Business Card Design needed - Something Awesome!

Need a business card designed. Company is "Harbor Vane Consulting" we do consulting and also have sales automation technology.
I'm going to use thick stock or metal, something really nice... I was thinking about a QR Code on the back that would just upload my contact info to the persons contact, etc -

This is a Strategy Company with a tech feel. I'm open to ideas but really want this to be nice!

I need a template that should include:

Name | Position or Title
D: 555.203.8146
www.harborvaneconsulting.example

I'm going to attach my contact so you can use that one, I need to get this printed.

Target Market(s)

Small to mid size customers, Entrepreneurs etc.

Industry/Entity Type

Consulting, Tech, Private Equity.

Contact Information for Business Card

Name, Phone, Maybe email, URL

Font styles to use
Sans Serif

Colors

Designer to choose only greyscale colors for use in the design.

Requirements
Must have
• Fresh, Clean, stand out from the crowd - will be on thick stock or metal.
Nice to have
• Clean, simple yet impactful.
Should not have
• Not cartoonish

```html
<!DOCTYPE html>
<html lang="en">
<head>
<meta charset="utf-8">
<title>Harbor Vane Consulting – Business Card</title>
<link rel="stylesheet" href="https://fonts.googleapis.com/css2?family=Inter:wght@400;500;700&display=swap">
<style>
  :root {
    --stage: #d9d9d9;
    --paper: #ffffff;
    --ink: #0b0b0c;
    --ink-soft: #1a1a1a;
    --silver-hi: #b9b9b9;
    --silver-lo: #3a3a3a;
    --reverse: #ffffff;
  }
  * { box-sizing: border-box; margin: 0; padding: 0; }
  html, body {
    width: 1200px; height: 1200px; overflow: hidden;
    background: var(--stage);
    font-family: "Inter", Arial, sans-serif;
    color: var(--ink);
  }
  .card {
    position: absolute;
    left: 161px;
    width: 878px;
    height: 513px;
  }
  .card--front { top: 66px; background: var(--paper); }
  .card--back { top: 629px; background: var(--ink); overflow: hidden; }

  .front-frame {
    position: absolute;
    left: 44px; top: 90px;
    width: 786px; height: 331px;
    border: 3px solid var(--ink);
    display: flex;
  }
  .brand-panel {
    width: 334px; height: 100%;
    background: var(--ink);
    display: flex; align-items: center; justify-content: center;
  }
  .brand-name {
    color: var(--reverse);
    font-weight: 700;
    font-size: 34px;
    letter-spacing: 1px;
  }
  .contact-block {
    flex: 1;
    padding: 34px 36px 0 0;
    text-align: right;
  }
  .person-name { font-weight: 700; font-size: 36px; line-height: 1.1; letter-spacing: -0.3px; }
  .person-title { font-weight: 400; font-size: 28px; line-height: 1.2; margin-top: 2px; }
  .meeting-link { font-weight: 400; font-size: 23px; margin-top: 30px; }
  .contact-list { list-style: none; margin-top: 44px; }
  .contact-item {
    display: flex; justify-content: flex-end; align-items: center;
    gap: 12px;
    font-size: 20px; line-height: 34px;
  }
  .contact-icon { width: 13px; height: 13px; flex: none; }

  .back-pattern {
    position: absolute; inset: 0;
    background:
      repeating-linear-gradient(90deg, rgba(0,0,0,0) 0 90px, var(--ink) 90px 140px),
      linear-gradient(180deg, var(--silver-lo), var(--silver-hi) 50%, var(--silver-lo));
    opacity: 0.55;
  }
  .back-wordmark-plate {
    position: absolute;
    left: 330px; top: 245px;
    width: 380px; height: 110px;
    background: var(--ink);
    display: flex; align-items: center; justify-content: center;
  }
  .back-wordmark {
    color: var(--reverse);
    font-weight: 500;
    font-size: 50px;
    letter-spacing: 1px;
    white-space: nowrap;
  }
</style>
</head>
<body>

<section class="card card--front" aria-label="Card front">
  <div class="front-frame">
    <div class="brand-panel">
      <span class="brand-name">HARBOR VANE</span>
    </div>
    <div class="contact-block">
      <h1 class="person-name">Daniel R. Hollis</h1>
      <p class="person-title">Founder / Owner</p>
      <p class="meeting-link">Book a Meeting</p>
      <ul class="contact-list">
        <li class="contact-item">555.203.8146
          <svg class="contact-icon" viewBox="0 0 16 16" aria-hidden="true">
            <path d="M3.5 1.5l2.5 0 1 3.5-1.6 1.2a8 8 0 0 0 4.4 4.4L11 9l3.5 1v2.5c0 1-1 2-2 2A11 11 0 0 1 1.5 3.5c0-1 1-2 2-2z" fill="var(--ink)"/>
          </svg>
        </li>
        <li class="contact-item">www.harborvaneconsulting.example
          <svg class="contact-icon" viewBox="0 0 16 16" aria-hidden="true">
            <circle cx="8" cy="8" r="6.5" fill="none" stroke="var(--ink)" stroke-width="1.6"/>
            <ellipse cx="8" cy="8" rx="2.8" ry="6.5" fill="none" stroke="var(--ink)" stroke-width="1.4"/>
            <line x1="1.5" y1="8" x2="14.5" y2="8" stroke="var(--ink)" stroke-width="1.4"/>
          </svg>
        </li>
      </ul>
    </div>
  </div>
</section>

<section class="card card--back" aria-label="Card back">
  <div class="back-pattern" role="img" aria-label="Repeating silver gradient brand pattern across the card"></div>
  <div class="back-wordmark-plate">
    <span class="back-wordmark">HARBOR VANE</span>
  </div>
</section>

</body>
</html>
```